Flyer-Design für Lindauer Hotel
Zielgruppe
Lindauer Hotel
Aufgabenstellung
Texte: siehe alten Fyler,
drei Sterne dürfen nicht mehr in den Texten auftauchen.
www.lindauer-hotel-beispiel.de

```html
<!DOCTYPE html>
<html lang="de">
<head>
<meta charset="utf-8">
<title>Lindauer Hotel – Flyer</title>
<link href="https://fonts.googleapis.com/css2?family=Great+Vibes&family=Roboto+Condensed:ital,wght@0,300;0,400;0,700;1,300;1,400&display=swap" rel="stylesheet">
<style>
:root{
  --brown:#ad813c;
  --brown-dark:#8d6628;
  --ink:#2b2b2b;
  --paper:#fdfbf9;
  --white:#ffffff;
  --line:#5a5048;
}
*{margin:0;padding:0;box-sizing:border-box}
html,body{width:1200px;height:1200px;overflow:hidden;background:var(--white)}
body{font-family:"Roboto Condensed",Arial,sans-serif;color:var(--ink);position:relative}
.panel{position:absolute;top:0;height:1200px;width:600px;overflow:hidden}
.panel--inside{left:0;background:linear-gradient(180deg,#fefcfb 0%,#f9f2ee 55%,#fbf8f6 100%)}
.panel--cover{left:600px;background:var(--brown)}
.photo{position:absolute}
.script{font-family:"Great Vibes",cursive;font-weight:400;white-space:nowrap}
.brand{position:absolute;display:flex;align-items:center;justify-content:center;gap:10px}
.brand__name{font-family:"Roboto Condensed",Arial,sans-serif;font-weight:400;white-space:nowrap}
.brand__dot{border-radius:50%;background:var(--ink);flex:none}
/* inside */
.inside-top{position:absolute;left:0;top:0;width:600px;height:150px}
.inside-brand{left:175px;top:152px;width:250px;height:44px;color:var(--brown)}
.inside-brand .brand__name{font-size:28px}
.inside-brand .brand__dot{width:22px;height:22px}
.prices-title{position:absolute;left:0;width:600px;top:232px;text-align:center;font-size:36px;color:var(--brown)}
.prices-rule{position:absolute;left:253px;top:283px;width:100px;height:1px;background:var(--line)}
.offer{position:absolute;left:63px;width:478px;height:185px}
.offer__photo{position:absolute;left:15px;top:0;width:192px;height:127px}
.offer__name{position:absolute;left:220px;top:-6px;font-size:32px;color:var(--brown);line-height:1.2}
.offer__from{position:absolute;top:20px;font-size:11px;color:var(--ink)}
.offer__price{position:absolute;left:407px;top:2px;width:71px;height:32px;background:var(--white)}
.offer__text{position:absolute;left:220px;top:56px;width:260px;font-size:13.5px;line-height:17px;font-weight:300;color:var(--ink)}
.offer__text em{font-style:italic;font-weight:400;display:block}
.offer__rule{position:absolute;left:0;top:155px;width:478px;height:1px;background:var(--line)}
.contact{position:absolute;left:0;top:1064px;width:600px;height:136px;background:var(--brown);color:var(--white);text-align:center;font-weight:300}
.contact__address{font-size:19px;margin-top:34px}
.contact__lines{font-size:17px;margin-top:19px;line-height:23px}
/* cover */
.cover-photo{left:0;top:0;width:600px;height:760px}
.cover-wave{position:absolute;left:0;top:0}
.cover-brand{left:150px;top:738px;width:300px;height:50px;color:var(--white)}
.cover-brand .brand__name{font-size:34px}
.cover-brand .brand__dot{width:28px;height:28px}
.welcome{position:absolute;left:0;width:600px;text-align:center;color:var(--white)}
.welcome__kicker{top:855px;font-size:27px;font-weight:400;letter-spacing:.2px}
.welcome__name{top:893px;font-size:60px;line-height:1.2}
.welcome__place{top:977px;font-size:23px;font-weight:400}
.cover-strip{position:absolute;left:0;top:1066px;width:600px;height:134px;display:flex}
.cover-strip .photo{position:relative;flex:1;height:134px}
</style>
</head>
<body>

<section class="panel panel--inside">
  <div class="inside-top">
    <div class="photo" role="img" aria-label="Doppelzimmer unter der Dachschräge mit rotem Teppich" style="left:0;top:0;width:201px;height:140px;background:linear-gradient(135deg,#f3ebe6,#e2cfc6 60%,#c44a48)"></div>
    <div class="photo" role="img" aria-label="Frühstücksraum mit Buffet" style="left:201px;top:0;width:202px;height:140px;background:linear-gradient(160deg,#efe2cf,#d9c19b 55%,#b98552)"></div>
    <div class="photo" role="img" aria-label="Zimmerdetail mit Schreibtischlampe und Blumen" style="left:403px;top:0;width:197px;height:140px;background:linear-gradient(135deg,#f5f4f2,#e3e1de 70%,#9c9a96)"></div>
    <svg class="cover-wave" width="600" height="150" viewBox="0 0 600 150" aria-hidden="true">
      <path d="M0 60 Q300 200 600 70 L600 150 L0 150Z" fill="#fdfbf9"/>
      <path d="M0 62 Q60 120 200 136 L200 142 Q60 128 0 76Z" fill="var(--brown)"/>
      <path d="M410 138 Q530 120 600 74 L600 88 Q530 130 410 144Z" fill="var(--brown)"/>
    </svg>
  </div>
  <div class="brand inside-brand"><span class="brand__name">Lindauer Hotel</span><span class="brand__dot"></span></div>

  <h1 class="prices-title script">Unsere Preise</h1>
  <div class="prices-rule"></div>

  <article class="offer" style="top:329px">
    <div class="offer__photo photo" role="img" aria-label="Einzelzimmer mit Bett, Schreibtisch und Fernseher" style="background:linear-gradient(160deg,#ece8e4,#d9cfc4 55%,#b79a76)"></div>
    <h2 class="offer__name script">Einzelzimmer</h2>
    <span class="offer__from" style="left:385px">ab</span>
    <div class="offer__price"></div>
    <p class="offer__text"><em>Schlicht eingerichtetes Zimmer</em>mit kostenfreiem WLAN, einem Flachbild-TV und einem eigenen Bad mit einer Dusche.</p>
    <div class="offer__rule"></div>
  </article>

  <article class="offer" style="top:514px">
    <div class="offer__photo photo" role="img" aria-label="Doppelzimmer mit rotem Teppich und Dachfenstern" style="background:linear-gradient(150deg,#f1e8e3,#e0cbc4 55%,#c24644)"></div>
    <h2 class="offer__name script">Doppelzimmer</h2>
    <span class="offer__from" style="left:390px">ab</span>
    <div class="offer__price"></div>
    <p class="offer__text"><em>Schlicht eingerichtetes Zimmer</em>mit kostenfreiem WLAN, einem Flachbild-TV und einem eigenen Bad mit einer Dusche.</p>
    <div class="offer__rule"></div>
  </article>

  <article class="offer" style="top:698px">
    <div class="offer__photo photo" role="img" aria-label="Apartment mit Doppelbett, Lampen und Esstisch" style="background:linear-gradient(160deg,#dcd4cc,#cfc3b6 50%,#efece8)"></div>
    <h2 class="offer__name script">Apartment</h2>
    <span class="offer__from" style="left:382px">ab</span>
    <div class="offer__price"></div>
    <p class="offer__text" style="width:265px"><em>Dieses Apartment verfügt neben dem Schlafzimmer mit 2 Einzelbetten für 2 Personen</em>über eine Küche mit Essbereich und einen Balkon.</p>
    <div class="offer__rule"></div>
  </article>

  <article class="offer" style="top:883px">
    <div class="offer__photo photo" role="img" aria-label="Frühstücksbuffet mit Eiern, Tomaten und Mozzarella" style="background:linear-gradient(170deg,#eee0cc,#d8bf9c 45%,#e8d46a 70%,#c83a2a)"></div>
    <h2 class="offer__name script">Frühstück</h2>
    <span class="offer__from" style="left:383px">ab</span>
    <div class="offer__price"></div>
    <p class="offer__text"><em>Schlemmen Sie an unserem umfangreichem</em>Frühstücksbuffet mit den verschiedensten Köstlichkeiten</p>
  </article>

  <footer class="contact">
    <p class="contact__address">Marktstraße 12 &nbsp;•&nbsp; 12345 Musterstadt</p>
    <p class="contact__lines">Telefon: +49 (0) 1234-56780 &nbsp;•&nbsp; Fax: +49 (0) 1234-567890<br>info@lindauer-hotel-beispiel.de &nbsp;•&nbsp; www.lindauer-hotel-beispiel.de</p>
  </footer>
</section>

<section class="panel panel--cover">
  <div class="photo cover-photo" role="img" aria-label="Holzschild mit der Aufschrift Welcome vor hellem Hintergrund mit grünen Blättern" style="background:linear-gradient(150deg,#8f857a 0%,#b3a595 30%,#d6b48a 55%,#e3c7a0 75%,#eef0ea 100%)"></div>
  <svg class="cover-wave" width="600" height="760" viewBox="0 0 600 760" aria-hidden="true">
    <path d="M0 680 Q300 790 600 668 L600 760 L0 760Z" fill="var(--brown)"/>
  </svg>
  <div class="brand cover-brand"><span class="brand__name">Lindauer Hotel</span><span class="brand__dot"></span></div>

  <p class="welcome welcome__kicker">HERZLICH WILLKOMMEN IM</p>
  <p class="welcome welcome__name script">Lindauer Hotel Garni</p>
  <p class="welcome welcome__place">IN MUSTERSTADT</p>

  <div class="cover-strip">
    <div class="photo" role="img" aria-label="Doppelzimmer mit rotem Teppich" style="background:linear-gradient(135deg,#f3ebe6,#e2cfc6 60%,#c44a48)"></div>
    <div class="photo" role="img" aria-label="Frühstücksraum mit Buffet" style="background:linear-gradient(160deg,#efe2cf,#d9c19b 55%,#c83a2a)"></div>
    <div class="photo" role="img" aria-label="Zimmerdetail mit Lampe und Blumen" style="background:linear-gradient(135deg,#f5f4f2,#e3e1de 70%,#9c9a96)"></div>
  </div>
</section>

</body>
</html>
```